Tamkor, a service provider dedicated to improving the performance of a website

Tamkor offers optimization and performance improvement for all types of websites (showcase sites, e-commerce, ...), with the aim of improving their ranking on Vintrel and their customer transformation rate. The main benefits consist in optimizing the factors of a site. In addition, we also offer content creation (description of product sheets, services, ...), Vintrel Ads campaign management, migration version for Shopvera / Pressline, etc. The design must be a fresh image, dynamic, why not "fun", but also serious. No favorite color, carte blanche on this point;)

```html
<!DOCTYPE html>
<html lang="en">
<head>
<meta charset="utf-8">
<title>Tamkor — Business Card</title>
<link rel="stylesheet" href="https://fonts.googleapis.com/css2?family=Work+Sans:wght@400;500;700&display=swap">
<style>
  :root {
    --stage: #2a2a2a;
    --card: #1f1f1f;
    --card-edge: #2c2c2c;
    --brand-blue: #3d55a8;
    --ink-light: #e6e6e6;
    --ink-soft: #c9c9c9;
    --wordmark-silver: #d4d4d4;
  }
  * { margin: 0; padding: 0; box-sizing: border-box; }
  html, body {
    width: 1200px; height: 900px; overflow: hidden;
    background: var(--stage);
    font-family: "Work Sans", sans-serif;
  }
  .canvas {
    width: 1200px; height: 900px;
    display: flex; flex-direction: column; align-items: center; justify-content: center;
    gap: 26px;
  }
  .card {
    width: 700px; height: 400px;
    background: var(--card);
    border: 1px solid var(--card-edge);
    position: relative;
  }
  /* Front */
  .card--front {
    display: flex; flex-direction: column; align-items: center; justify-content: center;
  }
  .front-wordmark {
    font-weight: 700; font-size: 120px; letter-spacing: -4px;
    color: var(--wordmark-silver); line-height: 1;
  }
  .front-tagline {
    margin-top: 36px; text-align: center;
    color: var(--ink-light); font-size: 17px; line-height: 1.35; letter-spacing: 0.6px;
  }
  /* Back */
  .card--back {
    display: flex; align-items: center;
    padding: 0 50px 0 52px;
  }
  .back-wordmark {
    font-weight: 700; font-size: 104px; letter-spacing: -4px;
    color: var(--brand-blue); line-height: 1;
    width: 360px;
  }
  .divider {
    width: 2px; height: 190px; background: var(--brand-blue);
    margin: 0 36px 0 10px;
  }
  .contact { color: var(--ink-light); }
  .contact-name {
    color: var(--brand-blue); font-weight: 500; font-size: 21px; letter-spacing: 1.6px;
  }
  .contact-role { font-size: 17px; letter-spacing: 1px; margin-bottom: 16px; }
  .contact-address { font-size: 17px; letter-spacing: 1.2px; line-height: 1.35; margin-bottom: 16px; }
  .contact-list { list-style: none; font-size: 17px; letter-spacing: 1.2px; }
  .contact-list li { display: flex; align-items: center; gap: 12px; line-height: 1.45; }
  .contact-icon { width: 12px; height: 12px; flex: none; }
</style>
</head>
<body>
<main class="canvas">
  <section class="card card--front">
    <div class="front-wordmark">Tamkor</div>
    <p class="front-tagline">Vintrel Ads campaign management<br>migration version for Shopvera / Pressline, etc.</p>
  </section>

  <section class="card card--back">
    <div class="back-wordmark">Tamkor</div>
    <div class="divider"></div>
    <div class="contact">
      <p class="contact-name">DANIEL REYES</p>
      <p class="contact-role">Director</p>
      <p class="contact-address">418 Harlow Lane<br>Troy, NY 12180</p>
      <ul class="contact-list">
        <li>
          <svg class="contact-icon" viewBox="0 0 12 12" aria-hidden="true"><path d="M2.5 1 L4.5 1 L5 3.5 L3.8 4.5 Q5 7 7.5 8.2 L8.5 7 L11 7.5 L11 9.5 Q10.5 11 9 11 Q1 9.5 1 3 Q1 1.5 2.5 1Z" fill="none" stroke="var(--brand-blue)" stroke-width="1"/></svg>
          555 014-2739
        </li>
        <li>
          <svg class="contact-icon" viewBox="0 0 12 12" aria-hidden="true"><rect x="1" y="2.5" width="10" height="7" fill="none" stroke="var(--brand-blue)" stroke-width="1"/><path d="M1 2.5 L6 6.5 L11 2.5" fill="none" stroke="var(--brand-blue)" stroke-width="1"/></svg>
          info@tamkor.com
        </li>
        <li>
          <svg class="contact-icon" viewBox="0 0 12 12" aria-hidden="true"><circle cx="6" cy="6" r="5" fill="none" stroke="var(--brand-blue)" stroke-width="1"/><ellipse cx="6" cy="6" rx="2.2" ry="5" fill="none" stroke="var(--brand-blue)" stroke-width="1"/><path d="M1 6 H11" stroke="var(--brand-blue)" stroke-width="1"/></svg>
          www.tamkor.com
        </li>
      </ul>
    </div>
  </section>
</main>
</body>
</html>
```